Email Signature

Our company is having its 10th anniversary in 2021. We would like a new email signature to celebrate the occasion. Attached is our business card design.
Please refer to our website for actual contact details.
www.tarvinestates.com.au

Industry/Entity Type

Real Estate

Requirements
Must have
• Our logo
Email
Contact Numbers
Address
Website address

Celebrating 10 years in 2021
Nice to have
• Something that blends the designs of our website and business card

```html
<!DOCTYPE html>
<html lang="en">
<head>
<meta charset="utf-8">
<title>Tarvine Estates – Email Signature</title>
<link rel="stylesheet" href="https://fonts.googleapis.com/css2?family=Roboto:wght@400;500;700;900&family=Kaushan+Script&display=swap">
<style>
  :root {
    --backdrop: #ebebeb;
    --paper: #ffffff;
    --brand-blue: #1f66ad;
    --ink: #1d1d1b;
    --text: #2b2b2b;
    --divider: #cfcfcf;
    --on-blue: #ffffff;
  }
  * { box-sizing: border-box; margin: 0; padding: 0; }
  html, body {
    width: 1200px; height: 653px; overflow: hidden;
    background: var(--backdrop);
    font-family: "Roboto", Arial, sans-serif;
  }
  .signature {
    position: absolute; left: 87px; top: 118px;
    width: 1013px; height: 412px;
    background: var(--paper);
    box-shadow: 4px 6px 10px rgba(0,0,0,0.35);
    overflow: hidden;
  }
  .brand {
    position: absolute; left: 24px; top: 196px; width: 360px;
    display: flex; align-items: center; justify-content: center; gap: 10px;
  }
  .brand-dot {
    width: 18px; height: 18px; border-radius: 50%;
    background: var(--brand-blue); flex: none;
  }
  .brand-name {
    font-weight: 700; font-size: 31px; line-height: 40px;
    color: var(--ink); white-space: nowrap;
  }
  .divider {
    position: absolute; top: 46px; width: 1px; height: 189px;
    background: var(--divider);
  }
  .divider--left { left: 406px; }
  .divider--right { left: 728px; }
  .contact {
    position: absolute; left: 430px; top: 48px;
    color: var(--text);
  }
  .contact-name {
    font-weight: 700; font-size: 21px; color: var(--brand-blue); line-height: 26px;
  }
  .contact-role { font-size: 19px; line-height: 26px; margin-bottom: 26px; }
  .contact-list { list-style: none; }
  .contact-list li {
    display: flex; align-items: center; gap: 9px;
    font-size: 19px; line-height: 26px;
  }
  .contact-list svg { width: 15px; height: 15px; fill: var(--brand-blue); flex: none; }
  .anniversary {
    position: absolute; left: 728px; top: 0; width: 285px; height: 270px;
  }
  .anniversary-number {
    position: absolute; left: 42px; top: 18px;
    font-weight: 900; font-size: 140px; line-height: 1; letter-spacing: -4px;
    color: var(--brand-blue);
  }
  .anniversary-years {
    position: absolute; left: 146px; top: 150px;
    font-weight: 500; font-size: 26px; line-height: 30px; color: var(--ink); letter-spacing: 0.5px;
  }
  .anniversary-title {
    position: absolute; left: 6px; top: 176px;
    font-family: "Kaushan Script", cursive;
    font-size: 44px; line-height: 56px; color: var(--ink); white-space: nowrap;
  }
  .anniversary-year {
    position: absolute; left: 100px; top: 232px;
    font-weight: 700; font-size: 22px; line-height: 26px; letter-spacing: 8px;
    color: var(--brand-blue);
  }
  .skyline {
    position: absolute; left: 0; bottom: 0; width: 100%; height: 150px;
    background: linear-gradient(to bottom, rgba(31,102,173,0) 0%, rgba(31,102,173,0.6) 18%, var(--brand-blue) 45%);
  }
  .address {
    position: absolute; left: 53px; top: 360px;
    font-size: 20px; line-height: 24px; color: var(--on-blue);
  }
  .social {
    position: absolute; left: 832px; top: 356px;
    display: flex; gap: 12px; list-style: none;
  }
  .social li {
    width: 32px; height: 32px; border-radius: 50%; background: var(--on-blue);
  }
</style>
</head>
<body>
  <main class="signature">
    <div class="brand">
      <span class="brand-dot"></span>
      <span class="brand-name">TARVINE ESTATES</span>
    </div>

    <span class="divider divider--left"></span>

    <section class="contact">
      <p class="contact-name">Dale Mercer</p>
      <p class="contact-role">Owner</p>
      <ul class="contact-list">
        <li>
          <svg viewBox="0 0 16 16" aria-hidden="true"><path d="M5 1h6a1 1 0 0 1 1 1v12a1 1 0 0 1-1 1H5a1 1 0 0 1-1-1V2a1 1 0 0 1 1-1zm.5 1.5v10h5v-10z"/></svg>
          561-555-712
        </li>
        <li>
          <svg viewBox="0 0 16 16" aria-hidden="true"><path d="M3.6 1.2l2.2 2.6c.3.4.3.9 0 1.3L4.7 6.3c.9 2 2.5 3.6 4.6 4.6l1.2-1.1c.4-.3.9-.3 1.3 0l2.6 2.2c.4.3.4.9.1 1.3l-1.2 1.3c-.5.5-1.2.7-1.9.5C6 13.6 2.4 10 .9 4.6.7 3.9.9 3.2 1.4 2.7l1.3-1.3c.3-.4.6-.4.9-.2z"/></svg>
          561-555-0190
        </li>
        <li>
          <svg viewBox="0 0 16 16" aria-hidden="true"><path d="M1 3h14v10H1zm1.4 1.2L8 8.6l5.6-4.4z"/></svg>
          dalemercer@mailbox.com
        </li>
        <li>
          <svg viewBox="0 0 16 16" aria-hidden="true"><path d="M8 1a7 7 0 1 0 0 14A7 7 0 0 0 8 1zm0 1.6c.7.8 1.3 2 1.5 3.4h-3C6.7 4.6 7.3 3.4 8 2.6zM2.7 9.3a5.4 5.4 0 0 1 0-2h2.3a11 11 0 0 0 0 2zm.6 1.4h2a8 8 0 0 0 1 2.6 5.4 5.4 0 0 1-3-2.6zm2-4.7h-2a5.4 5.4 0 0 1 3-2.6 8 8 0 0 0-1 2.6zM8 13.4c-.7-.8-1.3-2-1.5-2.7h3c-.2.7-.8 1.9-1.5 2.7zm1.7-4.1H6.3a9.6 9.6 0 0 1 0-2h3.4a9.6 9.6 0 0 1 0 2z"/></svg>
          www.tarvinestates.com.au
        </li>
      </ul>
    </section>

    <span class="divider divider--right"></span>

    <div class="skyline" role="img" aria-label="Blue city skyline silhouette across the base of the signature"></div>

    <section class="anniversary">
      <span class="anniversary-number">10</span>
      <span class="anniversary-years">YEARS</span>
      <span class="anniversary-title">Celebrating</span>
      <span class="anniversary-year">2021</span>
    </section>

    <p class="address">2240 s. Harbor Avenue #210, Palm Shore, Florida 33480</p>

    <ul class="social" aria-label="Social profiles">
      <li></li>
      <li></li>
      <li></li>
    </ul>
  </main>
</body>
</html>
```